Unique business card design

Boutique coastal hotel suites - in need of clever stand out business card I have uploaded the logo that I had created through quill forge I want something that is clever and stands out from everyone else - 418 Brantwell Avenue kelvane Alaska 99571 phone or text 907 -581-6142 www.primemarrowbysuites.com

Target Market(s)

Men and woman

Industry/Entity Type

Boutique coastal hotel

Contact Information for Business Card

Marrowby Suites kelvane Alaska marrowby_suites@mailnest.net

Requirements
Must have
• Classy - clever -bold 907-581-6142 call or text

```html
<!DOCTYPE html>
<html lang="en">
<head>
<meta charset="utf-8">
<title>Marrowby Suites – Business Card</title>
<link href="https://fonts.googleapis.com/css2?family=Montserrat:wght@600;700&family=Questrial&display=swap" rel="stylesheet">
<style>
  :root{
    --backdrop:#2a2a2a;
    --card:#f0ede6;
    --navy:#2d4e6e;
    --red:#d42a2a;
    --ink:#6b6b6b;
  }
  html,body{margin:0;padding:0;overflow:hidden}
  body{width:1200px;height:527px;background:var(--backdrop);position:relative;font-family:"Questrial",sans-serif}
  .card{position:absolute;width:461px;height:277px;background:var(--card);box-shadow:0 3px 8px rgba(0,0,0,.5)}
  .card-front{left:106px;top:126px}
  .card-back{left:634px;top:124px}
  .brand-name{position:absolute;left:0;right:0;top:122px;text-align:center;
    font-family:"Montserrat",sans-serif;font-weight:600;font-size:26px;color:var(--navy);letter-spacing:1px}
  .identity{position:absolute;right:306px;top:121px;text-align:right}
  .person-name{font-family:"Montserrat",sans-serif;font-weight:700;font-size:21px;color:var(--navy);line-height:1;letter-spacing:-.3px}
  .person-role{font-size:12.5px;color:var(--ink);margin-top:3px}
  .divider{position:absolute;left:162px;top:101px;width:1px;height:77px;background:#9a9a9a}
  .contact-list{position:absolute;left:172px;top:105px;margin:0;padding:0;list-style:none}
  .contact-list li{display:flex;align-items:center;height:17px;font-size:12.5px;color:var(--ink);white-space:nowrap}
  .contact-list svg{width:10px;height:10px;margin-right:6px;flex:none}
</style>
</head>
<body>
  <section class="card card-front">
    <div class="brand-name">Marrowby Suites</div>
  </section>

  <section class="card card-back">
    <div class="identity">
      <div class="person-name">JOHN DOE</div>
      <div class="person-role">Mangaer</div>
    </div>
    <div class="divider"></div>
    <ul class="contact-list">
      <li><svg viewBox="0 0 10 10"><circle cx="5" cy="5" r="5" fill="var(--red)"/><path d="M3 2.6c.4-.3.7-.2.9.2l.4.8c.1.3 0 .5-.2.7l-.3.2c.3.7.8 1.2 1.5 1.5l.2-.3c.2-.2.4-.3.7-.2l.8.4c.4.2.5.5.2.9-.4.6-1 .8-1.7.5C4.8 6.7 3.3 5.2 2.6 3.9c-.3-.6-.1-1 .4-1.3z" fill="#fff"/></svg>907 -581-6142</li>
      <li><svg viewBox="0 0 10 10"><circle cx="5" cy="5" r="5" fill="var(--red)"/><rect x="2.4" y="3.2" width="5.2" height="3.6" fill="#fff"/><path d="M2.4 3.2L5 5.3l2.6-2.1" fill="none" stroke="var(--red)" stroke-width=".6"/></svg>907 -581-6142</li>
      <li><svg viewBox="0 0 10 10"><circle cx="5" cy="5" r="5" fill="var(--red)"/><g fill="none" stroke="#fff" stroke-width=".6"><circle cx="5" cy="5" r="3"/><ellipse cx="5" cy="5" rx="1.3" ry="3"/><path d="M2 5h6M2.5 3.5h5M2.5 6.5h5"/></g></svg>www.primemarrowbysuites.com</li>
      <li><svg viewBox="0 0 10 10"><circle cx="5" cy="5" r="5" fill="var(--red)"/><path d="M5 2.3L2.3 4.8h.8v2.9h1.3V6h1.2v1.7h1.3V4.8h.8z" fill="#fff"/></svg>418 Brantwell Avenue kelvane Alaska 99571</li>
    </ul>
  </section>
</body>
</html>
```